We need a business card design for Corvana Group. We are a healthcare recruiting, wellness and education company. We partner with medical facilities to find quality candidates. We also offer free wellness courses.
The final design should communicate an emphasis on recruiting and wellness
The main purpose of the business card is to utilized it for networking events, give to hospitals, executives, VCs surgery centers and clinics. I want it to be sleek, clean, use of our brand colors and professional.

```html
<!DOCTYPE html>
<html lang="en">
<head>
<meta charset="utf-8">
<title>Corvana Group – Business Card</title>
<link href="https://fonts.googleapis.com/css2?family=Montserrat:wght@300;400;500;700&display=swap" rel="stylesheet">
<style>
  :root {
    --teal: #0a5f57;
    --teal-deep: #08524b;
    --teal-tone: #0d6c63;
    --paper: #ffffff;
    --stage: #e7e9e8;
    --ink: #0a5f57;
  }
  * { box-sizing: border-box; margin: 0; padding: 0; }
  html, body { width: 1200px; height: 900px; overflow: hidden; }
  body {
    background: var(--stage);
    font-family: "Montserrat", sans-serif;
    display: flex;
    flex-direction: column;
    align-items: center;
    justify-content: center;
    gap: 56px;
  }
  .card {
    width: 630px;
    height: 360px;
    border-radius: 22px;
    position: relative;
    overflow: hidden;
    box-shadow: 0 10px 30px rgba(0,0,0,0.12);
  }

  /* Back side */
  .card-back {
    background: var(--teal);
    display: flex;
    align-items: center;
    justify-content: center;
    gap: 22px;
  }
  .back-mark {
    width: 62px; height: 62px;
    border-radius: 10px;
    background: var(--teal-tone);
  }
  .back-name {
    font-weight: 300;
    font-size: 74px;
    letter-spacing: -1px;
    color: var(--teal-tone);
    line-height: 1;
  }

  /* Front side */
  .card-front {
    background: var(--paper);
    color: var(--ink);
  }
  .front-band {
    position: absolute;
    left: 0; bottom: 0;
    width: 100%; height: 18px;
  }
  .front-body {
    position: absolute;
    top: 78px; left: 56px; right: 40px;
    display: flex;
    align-items: center;
  }
  .brand {
    display: flex;
    align-items: center;
    gap: 14px;
    padding-right: 26px;
  }
  .brand-mark {
    width: 30px; height: 30px;
    border-radius: 5px;
    background: var(--teal);
  }
  .brand-name {
    font-weight: 400;
    font-size: 44px;
    letter-spacing: -1px;
    color: var(--teal);
    line-height: 1;
  }
  .divider {
    width: 1.5px;
    height: 150px;
    background: var(--teal);
  }
  .details {
    padding-left: 22px;
  }
  .person-name {
    font-weight: 700;
    font-size: 19px;
    color: var(--teal);
  }
  .person-role {
    font-weight: 400;
    font-size: 13px;
    color: #3a4a48;
    margin-bottom: 18px;
  }
  .contact-list { list-style: none; }
  .contact-list li {
    display: flex;
    align-items: center;
    gap: 10px;
    font-size: 13px;
    color: #2c3634;
    margin-bottom: 8px;
  }
  .contact-list svg { width: 14px; height: 14px; flex: none; }
  .address {
    position: absolute;
    left: 0; right: 0; bottom: 64px;
    text-align: center;
    font-size: 13px;
    color: #2c3634;
    letter-spacing: 0.2px;
  }
</style>
</head>
<body>

  <section class="card card-back" aria-label="Business card back">
    <div class="back-mark"></div>
    <div class="back-name">Corvana</div>
  </section>

  <section class="card card-front" aria-label="Business card front">
    <div class="front-body">
      <div class="brand">
        <div class="brand-mark"></div>
        <div class="brand-name">Corvana</div>
      </div>
      <div class="divider"></div>
      <div class="details">
        <p class="person-name">Daniel Whitcombe</p>
        <p class="person-role">Principal</p>
        <ul class="contact-list">
          <li>
            <svg viewBox="0 0 16 16" aria-hidden="true"><path fill="#0a5f57" d="M4 1.5l2.2 2.6-1.3 1.6c.8 1.9 2.3 3.4 4.2 4.2l1.6-1.3 2.6 2.2-1.3 2.4C7 13 3 9 1.6 2.8z"/></svg>
            303 555 0142
          </li>
          <li>
            <svg viewBox="0 0 16 16" aria-hidden="true"><rect x="1" y="3" width="14" height="10" rx="1" fill="#0a5f57"/><path d="M1.5 3.8L8 9l6.5-5.2" stroke="#fff" stroke-width="1.2" fill="none"/></svg>
            info@corvanagroup.com
          </li>
          <li>
            <svg viewBox="0 0 16 16" aria-hidden="true"><circle cx="8" cy="8" r="6.5" fill="none" stroke="#0a5f57" stroke-width="1.5"/><path d="M1.5 8h13M8 1.5c-2.5 3-2.5 10 0 13M8 1.5c2.5 3 2.5 10 0 13" stroke="#0a5f57" stroke-width="1.1" fill="none"/></svg>
            www.corvanagroup.com
          </li>
        </ul>
      </div>
    </div>
    <p class="address">2140 Larkspur Ave. Denver, CO 80206</p>
    <svg class="front-band" viewBox="0 0 630 18" preserveAspectRatio="none" aria-hidden="true">
      <polygon points="0,0 470,0 462,18 0,18" fill="#0a5f57"/>
      <polygon points="478,0 630,0 630,18 470,18" fill="#0a5f57"/>
    </svg>
  </section>

</body>
</html>
```